New Update: I am changing the title of the book and the back cover text. Title was too long before. Same style as before.
New Title: Under the Quiet Sky
New Subtitle: A Gardener’s Notes on Patience (italics on front cover)

Back cover text:
Under the Quiet Sky: A Gardener’s Notes on Patience offers clear, compassionate guidance for those recovering from total loss. Drawing from his experience as a Brennick Flood survivor, Tobias Quellhorst shares practical advice on insurance, rebuilding, and emotional healing, along with lessons in strength and community. This is not a book about tragedy; it’s about perseverance and renewal. Under the Quiet Sky is a trusted companion for anyone rebuilding life, home, and hope after disaster.

Font styles to use
Serif

Colors
EB3D1F
EC4F4E
F09395
F8D3D4
FCEDEE

Requirements
Should not have
• No pictures or anything related to fire on the cover.

```html
<!DOCTYPE html>
<html lang="en">
<head>
<meta charset="utf-8">
<title>Under the Quiet Sky — Book Cover</title>
<link rel="stylesheet" href="https://fonts.googleapis.com/css2?family=Noto+Serif:ital,wght@1,700&family=Playfair+Display:wght@400;500&display=swap">
<style>
  :root {
    --page: #ffffff;
    --cover-red: #ea1f26;
    --cover-red-deep: #c41c22;
    --cover-red-dark: #8e151a;
    --title-white: #ffffff;
    --accent-yellow: #ffe600;
  }
  * { margin: 0; padding: 0; box-sizing: border-box; }
  html, body {
    width: 1200px;
    height: 1200px;
    overflow: hidden;
    background: var(--page);
  }
  .canvas {
    position: relative;
    width: 1200px;
    height: 1200px;
  }
  .cover {
    position: absolute;
    left: 240px;
    top: 60px;
    width: 720px;
    height: 1080px;
    background: var(--cover-red);
    overflow: hidden;
    font-family: "Playfair Display", Georgia, serif;
    color: var(--title-white);
  }
  .cover__texture {
    position: absolute;
    inset: 0;
    width: 100%;
    height: 100%;
  }
  .cover__text {
    position: absolute;
    left: 0;
    width: 100%;
    text-align: center;
    white-space: nowrap;
    line-height: 1;
  }
  .title-lead {
    top: 0;
    font-size: 130px;
    font-weight: 500;
    letter-spacing: -1px;
  }
  .title-word {
    font-weight: 400;
  }
  .title-word--quiet {
    top: 122px;
    font-size: 220px;
    letter-spacing: -3px;
  }
  .title-word--sky {
    top: 315px;
    font-size: 300px;
    letter-spacing: 8px;
  }
  .tagline {
    top: 642px;
    font-size: 44px;
    font-weight: 400;
    letter-spacing: 5px;
    color: var(--accent-yellow);
  }
  .subtitle {
    top: 890px;
    font-family: "Noto Serif", Georgia, serif;
    font-size: 36px;
    font-style: italic;
    font-weight: 700;
  }
  .author {
    top: 984px;
    font-size: 50px;
    font-weight: 400;
    letter-spacing: 4px;
    color: var(--accent-yellow);
  }
  .back-copy[hidden] { display: none; }
</style>
</head>
<body>
<div class="canvas">
  <section class="cover" aria-describedby="back-copy">
    <svg class="cover__texture" viewBox="0 0 720 1080" role="img" aria-label="Soft abstract wash of deeper reds across the cover background">
      <defs>
        <radialGradient id="wash-left" cx="0" cy="0.4" r="0.55">
          <stop offset="0" stop-color="#8e151a" stop-opacity="0.55"/>
          <stop offset="1" stop-color="#ea1f26" stop-opacity="0"/>
        </radialGradient>
        <linearGradient id="wash-diagonal" x1="0" y1="1" x2="1" y2="0.4">
          <stop offset="0" stop-color="#c41c22" stop-opacity="0.35"/>
          <stop offset="0.5" stop-color="#c41c22" stop-opacity="0.15"/>
          <stop offset="1" stop-color="#ea1f26" stop-opacity="0"/>
        </linearGradient>
      </defs>
      <rect width="720" height="1080" fill="url(#wash-left)"/>
      <rect width="720" height="1080" fill="url(#wash-diagonal)"/>
    </svg>

    <div class="cover__text title-lead">under the</div>
    <div class="cover__text title-word title-word--quiet">QUIET</div>
    <div class="cover__text title-word title-word--sky">SKY</div>
    <div class="cover__text tagline">A Survivor’s Story</div>
    <div class="cover__text subtitle">A Gardener’s Notes on Patience</div>
    <div class="cover__text author">TOBIAS QUELLHORST</div>

    <p class="back-copy" id="back-copy" hidden>Under the Quiet Sky: A Gardener’s Notes on Patience offers clear, compassionate guidance for those recovering from total loss. Drawing from his experience as a Brennick Flood survivor, Tobias Quellhorst shares practical advice on insurance, rebuilding, and emotional healing, along with lessons in strength and community. This is not a book about tragedy; it’s about perseverance and renewal. Under the Quiet Sky is a trusted companion for anyone rebuilding life, home, and hope after disaster.</p>
  </section>
</div>
</body>
</html>
```